Tech Company requires UI design for mobile app

We need a mobile app design for a company based in Singapore called "Valdor Systems". We develop innovative Android/iOS business applications. KelmaRun - a collaboration tool targeted at SMEs that improves reporting and communication between different departments of an organisation. We would like to see designs that use the colour orange, our corporate colour. The final design should communicate clean and technology inclined design.

You are expected to recreate the icons, layout and structure without affecting the workflow.This is a workplace app for employee on mobile. The mobile app aims to empower individual employee to complete the following processes:

1. HR processes - taking attendance, timesheet, employment management to payslip)
2. Inventory management - stock taking, gift redemption and real-time stock management
3. Digital form - application for inspection, safety, procurement or request creation)
4. Job - an app that allows web portal to assign work to individual worker.
Updates

Project Deadline Extended
Reason: Received feedback to extens timeline. Cheers!

Target Market(s)

C-Executive, office employee, retail promoter, worker

Industry/Entity Type

Business

Colors

Designer to choose colors to be used in the design.

Requirements
Must have
• - Design must be neat, looks professional and perceived to be user-friendly
• - Use colour theme for each category
• - Must complement with KelmaRun logo them (already attached)
• - Have "apple" feel
• - We like the layout reference 1 & reference 2 photo. However, we prefer a better colour theme (Already Attached)
• - Please download the link for the work required
• https://files.quorvex.com/open?id=7Hq2LmPzXr4WtYb9NcKd3VfJsEa
Nice to have
• More info to follow shortly
Should not have
• - Must not be loud, flashy, dull, bored,
• - Design should not clash with Kelma Run Logo
• -

```html
<!DOCTYPE html>
<html lang="en">
<head>
<meta charset="utf-8">
<title>KelmaRun – Mobile App Screens</title>
<link href="https://fonts.googleapis.com/css2?family=Roboto:wght@300;400;500&display=swap" rel="stylesheet">
<style>
:root{
  --bg:#ffffff;
  --purple-top:#7a2ad8;
  --purple-bottom:#8574d9;
  --orange:#f07a2a;
  --ink:#333333;
  --muted:#6f6f6f;
  --light:#9a9a9a;
  --field-border:#d9d9de;
  --button:#8b85d6;
  --link:#1a7ef5;
  --panel-gray:#efeff3;
  --map-a:#e4e9dc;
  --map-b:#a9d3ee;
  --c-pin:#8d7ad8;--c-today:#5ac8fa;--c-records:#5a55d4;--c-stations:#7d5ad8;
  --c-new:#ff9500;--c-view:#ffcc00;--c-photo:#4cd964;--c-sales:#ff2d55;
  --c-check:#f0692a;--c-delivery:#3a87a6;--c-stock:#2aa39a;--c-list:#7ed321;
  --in:#ff2d55;--out:#4cd964;--locate:#5ac8fa;
}
*{box-sizing:border-box;margin:0;padding:0}
html,body{width:1200px;height:645px;overflow:hidden;background:var(--bg);font-family:"Roboto",Helvetica,Arial,sans-serif;color:var(--ink)}
.stage{position:absolute;left:0;top:0;width:1390px;height:747px;transform:scale(.8633);transform-origin:0 0}
.screen{position:absolute;top:48px;width:375px;height:667px;overflow:hidden;background:#fff;box-shadow:0 4px 18px rgba(0,0,0,.12)}
.screen--login{left:60px;background:linear-gradient(#f3f3fb,#ffffff 40%)}
.screen--home{left:512px}
.screen--attendance{left:963px}
.status-bar{position:absolute;top:0;left:0;right:0;height:22px;font-size:12px;display:flex;align-items:center;justify-content:space-between;padding:0 8px}
.status-bar .time{position:absolute;left:0;right:0;text-align:center}
.status-bar--light{color:#fff}
.header{position:absolute;left:0;top:0;width:100%;height:189px;background:linear-gradient(var(--purple-top),var(--purple-bottom));color:#fff}
.nav{position:absolute;top:22px;left:0;right:0;height:50px;border-bottom:1px solid rgba(255,255,255,.35);display:flex;align-items:center;padding:0 10px}
.nav .title{font-size:24px;font-weight:300}
.nav .title--center{position:absolute;left:0;right:0;text-align:center;font-size:21px;font-weight:400}
.nav .actions{margin-left:auto;display:flex;gap:16px;position:relative}
.profile{position:absolute;top:93px;left:18px;display:flex;align-items:center;gap:16px}
.avatar{width:72px;height:72px;border-radius:50%;border:2px solid #fff;background:radial-gradient(circle at 50% 40%,#d8c3b4,#6e6a6a)}
.profile .name{font-size:20px}
.profile .id{font-size:15px;opacity:.8;margin-top:4px}
.brand{position:absolute;top:180px;left:0;right:0;display:flex;justify-content:center;align-items:center;gap:10px}
.brand .dot{width:22px;height:22px;border-radius:50%;background:var(--orange)}
.brand .word{font-size:44px;font-weight:300;color:#555}
.field{position:absolute;left:42px;width:291px;height:43px;border:1px solid var(--field-border);border-radius:3px;background:#fff;padding:0 16px;font-size:15px;color:var(--light);display:flex;align-items:center}
.btn-login{position:absolute;left:42px;top:468px;width:291px;height:44px;border-radius:3px;background:var(--button);color:#fff;font-size:19px;display:flex;align-items:center;justify-content:center}
.register{position:absolute;top:524px;left:0;right:0;text-align:center;font-size:15px;color:var(--muted)}
.register a{color:var(--link);text-decoration:none}
.forgot{position:absolute;top:630px;left:0;right:0;text-align:center;font-size:15px;color:var(--muted)}
.home-body{position:absolute;top:189px;left:0;right:0;bottom:0;background:var(--panel-gray)}
.section{position:absolute;left:0;right:0;background:#fff;box-shadow:0 1px 3px rgba(0,0,0,.08)}
.section h2{font-size:18px;font-weight:300;color:var(--muted);text-align:center;position:absolute;left:0;right:0}
.tile{position:absolute;width:90px;margin-left:-45px;text-align:center;font-size:13px;color:var(--muted);line-height:17px;white-space:nowrap}
.tile .icon{width:40px;height:40px;border-radius:50%;margin:0 auto 6px;display:flex;align-items:center;justify-content:center}
.tile svg{width:22px;height:22px;fill:none;stroke:#fff;stroke-width:1.8;stroke-linecap:round;stroke-linejoin:round}
.tabbar{position:absolute;left:0;right:0;bottom:0;height:64px;background:#fff;display:flex;justify-content:space-around;align-items:center}
.tabbar svg{width:24px;height:24px;fill:none;stroke:#bdbdc2;stroke-width:1.6;stroke-linecap:round;stroke-linejoin:round}
.map{position:absolute;top:180px;left:0;right:0;bottom:0;background:linear-gradient(135deg,var(--map-a) 0%,var(--map-b) 45%,var(--map-a) 80%)}
.map-pin{position:absolute;left:118px;top:215px}
.locate{position:absolute;left:322px;top:277px;width:40px;height:40px;border-radius:50%;background:var(--locate);display:flex;align-items:center;justify-content:center}
.info-card{position:absolute;left:10px;top:325px;width:355px;height:269px;border-radius:3px;background:linear-gradient(135deg,#8a6fdc,#6f4fd6);color:#fff;font-size:16px}
.info-row{position:absolute;left:0;right:0;display:flex}
.info-row dt{width:120px;text-align:right;font-weight:400;opacity:.95}
.info-row dd{margin-left:23px;font-weight:500;line-height:22px}
.punch{position:absolute;top:609px;width:46px;height:46px;border-radius:50%;color:#fff;font-size:20px;display:flex;align-items:center;justify-content:center}
.punch--in{left:134px;background:var(--in)}
.punch--out{left:194px;background:var(--out)}
</style>
</head>
<body>
<div class="stage">

  <section class="screen screen--login">
    <div class="status-bar"><span>▮▮▮ Orbit</span><span class="time">9:41 AM</span><span>100% ▭</span></div>
    <div class="brand"><span class="dot"></span><span class="word">Valdor</span></div>
    <div class="field" style="top:287px">Username</div>
    <div class="field" style="top:347px">Password</div>
    <div class="btn-login">Login</div>
    <p class="register">Don’t have an account? <a href="#">Register Now</a></p>
    <p class="forgot">Forgot Password?</p>
  </section>

  <section class="screen screen--home">
    <header class="header">
      <div class="status-bar status-bar--light"><span>▮▮▮ Orbit</span><span class="time">9:41 AM</span><span>100% ▭</span></div>
      <div class="nav">
        <span class="title">KelmaRun</span>
        <div class="actions">
          <svg width="22" height="22" viewBox="0 0 24 24" fill="none" stroke="#fff" stroke-width="1.8"><path d="M6 17V11a6 6 0 0 1 12 0v6l2 2H4z"/><path d="M10 21h4"/><circle cx="19" cy="5" r="3" fill="#ff9500" stroke="none"/></svg>
          <svg width="22" height="22" viewBox="0 0 24 24" fill="none" stroke="#fff" stroke-width="1.8"><circle cx="12" cy="12" r="3"/><circle cx="12" cy="12" r="8" stroke-dasharray="4 2.3"/></svg>
        </div>
      </div>
      <div class="profile">
        <div class="avatar" role="img" aria-label="Employee profile photo"></div>
        <div><div class="name">Marcus Hale</div><div class="id">EM12456</div></div>
      </div>
    </header>
    <div class="home-body">
      <div class="section" style="top:0;height:147px">
        <h2 style="top:24px">Attendence</h2>
        <div class="tile" style="left:47px;top:63px"><div class="icon" style="background:var(--c-pin)"><svg viewBox="0 0 24 24"><path d="M12 21s-6-6-6-11a6 6 0 0 1 12 0c0 5-6 11-6 11z"/><circle cx="12" cy="10" r="2"/></svg></div>Take<br>Attendence</div>
        <div class="tile" style="left:143px;top:63px"><div class="icon" style="background:var(--c-today)"><svg viewBox="0 0 24 24"><circle cx="12" cy="12" r="8"/><path d="M12 8v4l3 2"/></svg></div>Today</div>
        <div class="tile" style="left:240px;top:63px"><div class="icon" style="background:var(--c-records)"><svg viewBox="0 0 24 24"><path d="M7 3h7l4 4v14H7z"/><path d="M10 12h5M10 15h5M10 18h3"/></svg></div>Past Records</div>
        <div class="tile" style="left:337px;top:63px"><div class="icon" style="background:var(--c-stations)"><svg viewBox="0 0 24 24"><circle cx="9" cy="9" r="3"/><path d="M3 19c0-3 3-5 6-5s6 2 6 5"/><path d="M15 6a3 3 0 0 1 0 6M18 14c2 1 3 3 3 5"/></svg></div>Stations</div>
      </div>
      <div class="section" style="top:151px;height:255px">
        <h2 style="top:20px">Sales &amp; Inventory</h2>
        <div class="tile" style="left:47px;top:60px"><div class="icon" style="background:var(--c-new)"><svg viewBox="0 0 24 24"><path d="M12 3l8 4v10l-8 4-8-4V7z"/><path d="M4 7l8 4 8-4M12 11v10"/></svg></div>New<br>Redemtion</div>
        <div class="tile" style="left:143px;top:60px"><div class="icon" style="background:var(--c-view)"><svg viewBox="0 0 24 24"><path d="M2 12s4-6 10-6 10 6 10 6-4 6-10 6S2 12 2 12z"/><circle cx="12" cy="12" r="3"/></svg></div>View<br>Redemtion</div>
        <div class="tile" style="left:240px;top:60px"><div class="icon" style="background:var(--c-photo)"><svg viewBox="0 0 24 24"><path d="M4 8h4l2-2h4l2 2h4v11H4z"/><circle cx="12" cy="13" r="3"/></svg></div>Take<br>Photo</div>
        <div class="tile" style="left:337px;top:60px"><div class="icon" style="background:var(--c-sales)"><svg viewBox="0 0 24 24"><path d="M3 17l6-6 4 4 8-8"/><path d="M15 7h6v6"/></svg></div>Sales<br>Summary</div>
        <div class="tile" style="left:47px;top:160px"><div class="icon" style="background:var(--c-check)"><svg viewBox="0 0 24 24"><circle cx="12" cy="12" r="8"/><path d="M8 12l3 3 5-6"/></svg></div>Inventory<br>Check</div>
        <div class="tile" style="left:143px;top:160px"><div class="icon" style="background:var(--c-delivery)"><svg viewBox="0 0 24 24"><path d="M3 5h3l2 10h10l2-7H7"/><circle cx="9" cy="19" r="1.4"/><circle cx="17" cy="19" r="1.4"/></svg></div>Delivery</div>
        <div class="tile" style="left:240px;top:160px"><div class="icon" style="background:var(--c-stock)"><svg viewBox="0 0 24 24"><path d="M4 4h8l8 8-8 8-8-8z"/><circle cx="8.5" cy="8.5" r="1.3"/></svg></div>New Stock<br>Take</div>
        <div class="tile" style="left:334px;top:160px"><div class="icon" style="background:var(--c-list)"><svg viewBox="0 0 24 24"><path d="M6 5h12v16H6z"/><path d="M9 3h6v4H9z"/></svg></div>Stock Take<br>List</div>
      </div>
      <nav class="tabbar">
        <svg viewBox="0 0 24 24"><path d="M4 11l8-7 8 7v10H4z"/><path d="M10 21v-6h4v6"/></svg>
        <svg viewBox="0 0 24 24"><circle cx="12" cy="8" r="4"/><path d="M4 21c0-4 4-6 8-6s8 2 8 6"/></svg>
        <svg viewBox="0 0 24 24"><rect x="4" y="5" width="16" height="16"/><path d="M4 10h16M8 3v4M16 3v4"/></svg>
        <svg viewBox="0 0 24 24"><path d="M20 12a8 8 0 0 1-14 5M4 12a8 8 0 0 1 14-5"/><path d="M18 3v4h-4M6 21v-4h4"/></svg>
      </nav>
    </div>
  </section>

  <section class="screen screen--attendance">
    <div class="map" role="img" aria-label="City street map around the employee's current location"></div>
    <svg class="map-pin" width="36" height="48" viewBox="0 0 36 48"><ellipse cx="18" cy="44" rx="14" ry="4" fill="#fff"/><path d="M18 40S4 26 4 17a14 14 0 0 1 28 0c0 9-14 23-14 23z" fill="#fff" stroke="#7a5ad8" stroke-width="2"/><circle cx="18" cy="17" r="5" fill="none" stroke="#7a5ad8" stroke-width="2"/></svg>
    <div class="locate"><svg width="24" height="24" viewBox="0 0 24 24" fill="none" stroke="#fff" stroke-width="1.8"><circle cx="12" cy="12" r="7"/><circle cx="12" cy="12" r="2"/><path d="M12 2v4M12 18v4M2 12h4M18 12h4"/></svg></div>
    <header class="header">
      <div class="status-bar status-bar--light"><span>▮▮▮ Orbit</span><span class="time">9:41 AM</span><span>100% ▭</span></div>
      <div class="nav">
        <svg width="22" height="22" viewBox="0 0 24 24" fill="none" stroke="#fff" stroke-width="2"><path d="M20 12H5M11 6l-6 6 6 6"/></svg>
        <span class="title title--center">Attendence</span>
        <div class="actions"><svg width="22" height="22" viewBox="0 0 24 24" fill="none" stroke="#fff" stroke-width="1.8"><circle cx="12" cy="12" r="3"/><circle cx="12" cy="12" r="8" stroke-dasharray="4 2.3"/></svg></div>
      </div>
      <div class="profile">
        <div class="avatar" role="img" aria-label="Employee profile photo"></div>
        <div><div class="name">Marcus Hale</div><div class="id">EM12456</div></div>
      </div>
    </header>
    <dl class="info-card">
      <div class="info-row" style="top:18px"><dt>Location:</dt><dd>Harbor Bridge</dd></div>
      <div class="info-row" style="top:66px"><dt>Last Seen:</dt><dd>Just Now</dd></div>
      <div class="info-row" style="top:114px"><dt>Project Mode</dt><dd>Offline</dd></div>
      <div class="info-row" style="top:163px"><dt>Project Info:</dt><dd>Project 2457 Harbor</dd></div>
      <div class="info-row" style="top:212px"><dt>Last Action:</dt><dd>Cloak in<br>24 Oct, 2017 10:33 am</dd></div>
    </dl>
    <div class="punch punch--in">in</div>
    <div class="punch punch--out">out</div>
  </section>

</div>
</body>
</html>
```